Print on top the name of the company: (Or Similar)
Larkmoor Cleaning & Disinfecting
Because your standards aren't standard.

We adhere to ALL NVB guidelines for both residential and commercial cleaning.

Infection Control is our ultimate goal.

Instructions:
Opening a residential and commercial cleaning and disinfecting company in south Florida.

Targeting high-end residential clients, commercial and healthcare facilities, specializing in Ambulatory Care Guidelines. With a concentration and expertise in targeting Covid 19 and other transmissible pathogens.

UMRE trained.
Owned and operated by a licensed BSN Registered Nurse specially ​trained in Infection Control Prevention with over 25 years experience. Over two decades in Ambulatory Surgery Center Administration, Director of Nursing and Infection Control Prevention ad Consulting.

Looking to create a business flier that emphasizes Cleaning & Disinfection
along with the standard expectation for residential and Commercial cleaning services
Updates

Need extra days to review

Target Market(s)

Residential & Commercial

Font styles to use
Decorative

Requirements
Must have
• A checklist for cleaning services

```html
<!DOCTYPE html>
<html lang="en">
<head>
<meta charset="utf-8">
<title>Larkmoor Cleaning &amp; Disinfecting – Flyer</title>
<link rel="stylesheet" href="https://fonts.googleapis.com/css2?family=Bebas+Neue&family=Montserrat:wght@500;600;700;800&display=swap">
<style>
  :root {
    --navy: #2b2d6b;
    --sky: #2a8fc6;
    --sheet: #e9e9ef;
    --paper: #ffffff;
    --ink: #111118;
    --photo-light: #cfe3ec;
    --photo-mid: #7fa9bd;
    --photo-dark: #3e5a66;
  }
  * { box-sizing: border-box; margin: 0; padding: 0; }
  html, body { width: 737px; height: 1200px; overflow: hidden; }
  body { background: var(--paper); font-family: "Montserrat", sans-serif; }

  .flyer {
    position: relative;
    width: 737px; height: 1200px;
    background: var(--paper);
    padding: 10px;
  }
  .sheet {
    position: relative;
    width: 100%; height: 100%;
    background: var(--sheet);
    overflow: hidden;
  }

  /* Hero */
  .hero-photo {
    position: absolute;
    left: 300px; top: 0;
    width: 417px; height: 420px;
    background: linear-gradient(90deg, var(--sheet) 0%, var(--photo-light) 22%, var(--photo-mid) 60%, var(--photo-dark) 100%);
  }
  .brand {
    position: absolute;
    left: 20px; top: 72px;
    font-family: "Bebas Neue", sans-serif;
    color: var(--navy);
    line-height: 0.95;
  }
  .brand .line-1 { display: block; font-size: 49px; }
  .brand .line-2 { display: block; font-size: 62px; }
  .goal {
    position: absolute;
    left: 20px; top: 218px;
    font-weight: 700;
    font-size: 23px;
    line-height: 1.2;
    color: var(--sky);
  }
  .adherence {
    position: absolute;
    left: 22px; top: 302px;
    width: 330px;
    font-weight: 600;
    font-size: 13.5px;
    line-height: 1.4;
    color: var(--ink);
  }

  /* Info band */
  .info-band {
    position: absolute;
    left: 0; top: 430px;
    width: 100%; height: 80px;
    background: linear-gradient(90deg, var(--sky) 0%, var(--navy) 75%);
    color: var(--paper);
    display: flex; align-items: center;
  }
  .info-band p {
    flex: 1;
    font-size: 13px;
    font-weight: 500;
    line-height: 1.35;
    padding: 0 18px 0 30px;
  }
  .info-band strong { font-weight: 700; }
  .info-band .divider {
    width: 2px; height: 56px; background: var(--paper);
  }

  /* Service panels */
  .service-panel {
    position: absolute;
    top: 536px;
    width: 330px; height: 428px;
    background: var(--sky);
    color: var(--paper);
    text-align: center;
  }
  .service-panel.commercial { left: 17px; }
  .service-panel.residential { left: 370px; }
  .service-panel h2 {
    font-family: "Bebas Neue", sans-serif;
    font-weight: 400;
    font-size: 52px;
    letter-spacing: 0.5px;
    margin-top: 14px;
    line-height: 1;
  }
  .service-list {
    list-style: none;
    margin-top: 10px;
    font-weight: 500;
    font-size: 15.5px;
    line-height: 27.6px;
  }

  /* Photo circles */
  .photo-circle {
    position: absolute;
    top: 878px;
    width: 200px; height: 200px;
    border-radius: 50%;
    border: 7px solid var(--paper);
    box-shadow: 0 4px 10px rgba(0,0,0,0.35);
  }
  .photo-circle.office { left: 53px; background: radial-gradient(circle at 60% 55%, var(--photo-mid), var(--photo-dark)); }
  .photo-circle.living-room { left: 262px; background: radial-gradient(circle at 50% 45%, #f1efe9, #b9c3c9); }
  .photo-circle.hallway { left: 470px; background: radial-gradient(circle at 55% 50%, #c9c9c4, #3b3f44); }

  /* Call band */
  .call-band {
    position: absolute;
    left: 0; top: 1118px;
    width: 100%; height: 46px;
    background: var(--navy);
    color: var(--paper);
    font-family: "Bebas Neue", sans-serif;
    font-size: 36px;
    letter-spacing: 1.5px;
    text-align: center;
    line-height: 48px;
  }
</style>
</head>
<body>
<main class="flyer">
  <div class="sheet">
    <div class="hero-photo" role="img" aria-label="Worker in a white protective suit spraying disinfectant along a bright glass-walled corridor"></div>

    <h1 class="brand">
      <span class="line-1">LARKMOOR CLEANING</span>
      <span class="line-2">&amp; DISINFECTING</span>
    </h1>
    <p class="goal">INFECTION CONTROL IS<br>OUR ULTIMATE GOAL</p>
    <p class="adherence">We adhere to ALL NVB guidelines for both residential and commercial cleaning.</p>

    <section class="info-band">
      <p>Opening a residential and commercial cleaning and disinfecting company in <strong>SOUTH FLORIDA.</strong></p>
      <span class="divider"></span>
      <p>Targeting high-end residential clients, commercial and healthcare facilities, specializing in Ambulatory Care Guidelines.</p>
    </section>

    <section class="service-panel commercial">
      <h2>COOMERCIAL</h2>
      <ul class="service-list">
        <li>JANITORIAL</li>
        <li>OFFICES</li>
        <li>FLOOR MAINTENANCE</li>
        <li>CARPET CLEANING</li>
        <li>MOVE-INS</li>
        <li>MOVE-OUTS.</li>
        <li>CONSTRUCTIONS CLEAN-UPS</li>
        <li>ESTATE CLEAN-OUTS</li>
      </ul>
    </section>

    <section class="service-panel residential">
      <h2>RESIDENTIAL</h2>
      <ul class="service-list">
        <li>HOUSE CLEANING</li>
        <li>BEFORE AND AFTER PARTY</li>
        <li>MOVE-INS</li>
        <li>MOVE-OUTS</li>
        <li>HOLIDAY CLEANING</li>
        <li>SEASONAL CLEANING</li>
        <li>CARPET CLEANING</li>
        <li>DEODORIZING AND SANITIZING</li>
      </ul>
    </section>

    <div class="photo-circle office" role="img" aria-label="Worker in protective gear fogging an office space with a blue sprayer"></div>
    <div class="photo-circle living-room" role="img" aria-label="Two workers in protective suits disinfecting a bright living room with green sprayers"></div>
    <div class="photo-circle hallway" role="img" aria-label="Worker in protective suit and respirator spraying a hallway doorway"></div>

    <footer class="call-band">PLEASE CALL US AT: (555) 274 19 36</footer>
  </div>
</main>
</body>
</html>
```